Professional, polished website design for boutique wealth management firm

Hello, thank you for your interest. PLEASE READ THE BRIEF BEFORE SUBMITTING THE DESIGN.-
PLEASE USE THE ATTACHED HOME PAGE COPY FOR THIS DESIGN.
We are looking for a professional, polished design that helps portray trust and credibility for a well-established independent wealth management firm. We have copy we've written for the home page and we'd like the design and imagery to play up the copy, so there's a better chance someone will read it all. So the headlines etc should all be easy to read and the design should draw the eye towards them. For colors, again trust is important so probably blue as a dominant color, but you can also use gray, green, etc. We'd like to avoid too much use of the color red (due to financial, association with loss). SO PLEASE AVOID USE OF THE COLOR RED. We also like bright orange or yellow for call to action buttons.

Please keep the design EASY TO MAINTAIN in wordpress as well.

I have attached home page copy as well as logo files.

Here's some sites that we like so feel free to use as inspiration:
https://www.brovaltcapitalworks.example/, https://harborpathpensionsplains.example/
https://tavrin-oakes.example/, https://plantfornextyear.example/, https://ferngatefinancial.example/

As another option/idea, I like the idea of a simple format with a clean image similar to this for the home page: https://www.pixmeadowstock.example/detail/photo/calculator-falling-royalty-free-image/31684207?adppopup=true
Just an idea.

Also please be sure to incorporate the QWA /Accredited Wealth Steward logo as well, farther down the page is fine.

Thank you for your help! Feel free to contact me with any questions.

Target Market(s)

Individuals aged 48-62 who are looking to maximize their wealth, such as business owners, executives, engineers, successful tradespeople, etc.

Industry/Entity Type

Finance--wealth management

Font styles to use
Sans Serif

Requirements
Must have
• Professional and polished, Call to action buttons must be clear and stand out, headlines must be clear and stand out, also text must be big enough to be easily readable by most people
Should not have
• Anything casual, frilly, etc.

```html
<!DOCTYPE html>
<html lang="en">
<head>
<meta charset="utf-8">
<title>Bulwark Asset Advisors</title>
<link href="https://fonts.googleapis.com/css2?family=Roboto+Condensed:wght@400;700&family=Lato:wght@400;700&display=swap" rel="stylesheet">
<style>
:root{
  --blue:#2a3a8f;
  --ink:#2b2b2b;
  --orange:#ff5a1f;
  --amber:#f7931e;
  --paper:#ffffff;
  --night:#000000;
}
*{margin:0;padding:0;box-sizing:border-box}
html,body{width:1200px;height:3636px;overflow:hidden;background:var(--paper)}
body{font-family:'Lato',sans-serif;color:var(--ink)}
.page{position:relative;width:1200px;height:3636px}
h1,h2,h3{font-family:'Roboto Condensed',sans-serif;font-weight:400;color:var(--blue)}

/* header */
.site-header{position:absolute;left:0;top:0;width:1200px;height:106px;background:var(--paper)}
.brand{position:absolute;left:151px;top:24px;display:flex;align-items:center;gap:10px;color:var(--blue);font-weight:700}
.brand-dot{width:44px;height:44px;border-radius:50%;background:var(--blue)}
.brand-name{font-size:30px;line-height:30px;letter-spacing:1px}
.brand-sub{font-size:16px;line-height:18px;padding-left:24px}
.header-contact{position:absolute;right:150px;top:16px;display:flex;gap:24px;font-size:14px;color:var(--blue)}
.header-contact span{display:flex;align-items:center;gap:8px}
.header-rule{position:absolute;left:466px;top:58px;width:584px;height:1px;background:#d9d9d9}
.main-nav{position:absolute;left:469px;top:76px;font-family:'Roboto Condensed',sans-serif;font-size:14.5px;color:var(--ink)}
.main-nav a{position:absolute;white-space:nowrap;color:inherit;text-decoration:none}
.main-nav a.current{color:var(--blue)}

/* hero */
.hero{position:absolute;left:0;top:106px;width:1200px;height:449px;background:linear-gradient(100deg,#3b3a36 0%,#6a6458 35%,#b29a8f 60%,#d8b7b5 80%,#c9a59b 100%)}
.hero-photo{position:absolute;inset:0;background:linear-gradient(180deg,rgba(255,255,255,0) 0%,rgba(120,110,70,.35) 100%)}
.hero-title{position:absolute;left:151px;top:84px;font-size:38px;line-height:48px;font-weight:700;color:#fff;white-space:nowrap}
.hero-text{position:absolute;left:151px;top:190px;font-size:14px;line-height:27px;font-weight:700;color:#fff;white-space:nowrap}
.btn{position:absolute;display:flex;align-items:center;justify-content:center;color:#fff;font-size:15px;text-decoration:none;white-space:nowrap}
.btn-orange{background:var(--orange)}
.btn-blue{background:var(--blue)}

/* intro */
.section-title{position:absolute;left:0;width:1200px;text-align:center;font-size:30px;line-height:39px;white-space:nowrap}
.divider{position:absolute;width:60px;height:2px;background:#222}
.divider::before{content:"";position:absolute;left:0;top:0;width:18px;height:2px;background:#bbb}
.centered-copy{position:absolute;left:0;width:1200px;text-align:center;font-size:14px;line-height:27px;white-space:nowrap}

/* strategies */
.strategies{position:absolute;left:0;top:935px;width:1200px;height:1399px;background:radial-gradient(ellipse at 50% 40%,#fbfbfb 0%,#ececec 55%,#e4e4e4 100%)}
.photo{position:absolute}
.frame{position:absolute;border:2px solid #222}
.feature-title{position:absolute;font-family:'Roboto Condensed',sans-serif;font-weight:700;font-size:21px;color:var(--blue)}
.feature-text{position:absolute;font-size:12.5px;line-height:24px;white-space:nowrap}

/* solutions */
.solution-card{position:absolute;top:2492px;width:165px;height:123px;background:linear-gradient(180deg,#f7f7f7,#e3e3e3);display:flex;align-items:center;justify-content:center}
.solution-card.active{background:linear-gradient(180deg,#ff7a2a,#ff4d14)}
.solution-label{position:absolute;top:2624px;width:165px;text-align:center;font-size:16px;line-height:24px;color:var(--ink)}

/* checkup */
.checkup{position:absolute;left:0;top:2736px;width:1200px;height:495px;background:linear-gradient(180deg,#efefef,#f8f8f8)}
.checkup-title{position:absolute;left:151px;top:2840px;font-size:33px;line-height:40px}
.checkup-text{position:absolute;left:151px;font-size:14px;line-height:24px;white-space:nowrap}

/* footer */
.site-footer{position:absolute;left:0;top:3231px;width:1200px;height:405px;background:var(--night);color:#fff}
.footer-brand{position:absolute;left:151px;top:52px;display:flex;align-items:center;gap:8px;color:var(--blue);font-weight:700}
.footer-brand .brand-dot{width:34px;height:34px}
.footer-about{position:absolute;left:151px;top:128px;font-size:11.5px;line-height:24px;white-space:nowrap}
.footer-head{position:absolute;top:62px;font-size:16px;color:var(--amber)}
.quick-links{position:absolute;left:565px;top:112px;list-style:none;font-size:13px;line-height:28px}
.quick-links li::before{content:"•";margin-right:8px}
.contact-row{position:absolute;left:784px;display:flex;gap:14px;font-size:13.5px;line-height:21px}
.contact-icon{width:48px;height:48px;border:1px solid #fff;display:flex;align-items:center;justify-content:center;flex:none}
.copyright{position:absolute;left:151px;top:364px;font-size:12.5px}
.badge{position:absolute;left:863px;top:349px;width:187px;height:46px;border:2px solid #fff;border-radius:3px}
</style>
</head>
<body>
<div class="page">

  <header class="site-header">
    <div class="brand">
      <div class="brand-dot"></div>
      <div><div class="brand-name">BULWARK</div><div class="brand-sub">Asset Advisors</div></div>
    </div>
    <div class="header-contact">
      <span><svg width="18" height="18" viewBox="0 0 24 24" fill="none" stroke="#ff5a1f" stroke-width="2"><path d="M5 3h4l2 5-3 2a12 12 0 0 0 6 6l2-3 5 2v4a2 2 0 0 1-2 2A18 18 0 0 1 3 5a2 2 0 0 1 2-2z"/></svg>123-456-7890</span>
      <span><svg width="20" height="18" viewBox="0 0 24 20" fill="none" stroke="#ff5a1f" stroke-width="2"><rect x="2" y="3" width="20" height="14"/><path d="M2 3l10 8 10-8"/></svg>info@bulwarkassetadvisors.example</span>
    </div>
    <div class="header-rule"></div>
    <nav class="main-nav">
      <a class="current" style="left:0">Tax Planning</a>
      <a style="left:97px">Our Strategies</a>
      <a style="left:203px">Solutions</a>
      <a style="left:285px">Retirement Check-Up</a>
      <a style="left:432px">Resources</a>
      <a style="left:515px">Contact Us</a>
    </nav>
  </header>

  <section class="hero">
    <div class="hero-photo" role="img" aria-label="Photo of a smiling couple walking a dog across a grassy hillside at sunset"></div>
    <h1 class="hero-title">The Most Effective Financial<br>Plans Start With Tax Planning</h1>
    <p class="hero-text">Few Financial Advisors Offer Tax Expertise, But When They<br>Do, You Benefit.&nbsp; Learn How Our Unique Team Combines<br>Financial Planning, Investments And Smart Tax And Income<br>Generation Strategies To Help You Achieve Your Goals Faster.</p>
    <a class="btn btn-orange" style="left:151px;top:312px;width:210px;height:42px">Learn Why We're Different</a>
  </section>

  <section class="intro">
    <h2 class="section-title" style="top:626px">Cookie-cutter Financial Planning And Investment Can<br>Leave Your Future At Risk.&nbsp; That's Why We Do It Differently.</h2>
    <div class="divider" style="left:560px;top:716px"></div>
    <p class="centered-copy" style="top:735px">You need better strategies in today's complex financial landscape.&nbsp; At Bulwark Asset Advisors, we bring financial planning,<br>investment management, retirement income, tax and estate planning expertise together under one roof.&nbsp;&nbsp; Our unique team<br>works together to help you make the most of your resources.</p>
    <a class="btn btn-orange" style="left:511px;top:834px;width:178px;height:44px">Meet Our Specialists</a>
  </section>

  <section class="strategies">
    <h2 class="section-title" style="top:72px">Better Strategies To Preserve and Grow Wealth,<br>Generate Income And Reduce Your Taxes</h2>
    <div class="divider" style="left:561px;top:164px"></div>
    <p class="centered-copy" style="top:178px;font-size:14.5px">Here's what you can expect when you work with Bulwark.</p>

    <div class="frame" style="left:138px;top:274px;width:350px;height:309px;border-right:none;border-top:none"></div>
    <div class="photo" role="img" aria-label="Photo of hands with a pen and calculator reviewing financial charts" style="left:147px;top:245px;width:414px;height:331px;background:linear-gradient(135deg,#f4d9a8 0%,#f6efe2 40%,#dfe6ee 75%,#b9c9da 100%)"></div>
    <h3 class="feature-title" style="left:606px;top:322px">A Better Approach</h3>
    <p class="feature-text" style="left:606px;top:360px">Taxes are critical to every financial move you make, so we incorporate<br>tax planning in everything we do for you. Along with managing your<br>investment, we help you safely generate retirement income, reduce<br>capital gains and minimize income taxes.&nbsp; We'll also help you with<br>estate planning strategies so you can protect your family's future and<br>make the most of opportunities.</p>

    <div class="frame" style="left:700px;top:646px;width:356px;height:310px;border-left:none;border-top:none"></div>
    <div class="photo" role="img" aria-label="Photo of an advisor meeting a couple at a white table with a laptop" style="left:634px;top:618px;width:414px;height:332px;background:linear-gradient(135deg,#e9e4da 0%,#f4f1ec 45%,#d8cfc3 100%)"></div>
    <h3 class="feature-title" style="left:151px;top:694px">More Experience</h3>
    <p class="feature-text" style="left:151px;top:733px">You've worked hard to get where you are, so your money shouldn't<br>have to be part of anyone's learning curve.&nbsp; At Bulwark Asset<br>Advisors, you'll only work with seasoned experts, each with<br>decades of investment, planning or tax experience.&nbsp; Our team<br>works together to help solve your financial challenges and get your<br>money working harder for you.</p>

    <div class="frame" style="left:141px;top:1028px;width:349px;height:310px;border-right:none;border-top:none"></div>
    <div class="photo" role="img" aria-label="Photo of a laptop and tablet showing charts on a wooden desk" style="left:150px;top:1001px;width:413px;height:330px;background:linear-gradient(135deg,#d8c99a 0%,#b8a57a 40%,#e8e2d4 70%,#c7b08a 100%)"></div>
    <h3 class="feature-title" style="left:607px;top:1081px">On Your Side</h3>
    <p class="feature-text" style="left:607px;top:1115px">In an industry rife with conflicts of interest, you need a firm that works<br>in your best interest.&nbsp; As an independent firm, we have no ties to<br>insurance or mutual fund companies.&nbsp; We're fee based, meaning<br>we're compensated by fees, not commissions.&nbsp; We also act as your<br>fiduciary, so we're ethically bound to put your interests first.&nbsp; That way,<br>you get our best advice...not product recommendations.</p>
  </section>

  <section class="solutions">
    <h2 class="section-title" style="top:2405px">Personalized Solutions To Help Your Money Work Harder For You</h2>
    <div class="divider" style="left:617px;top:2462px"></div>

    <div class="solution-card" style="left:150px"><svg width="70" height="64" viewBox="0 0 70 64" fill="none" stroke="#222" stroke-width="2"><circle cx="48" cy="14" r="8"/><path d="M12 58h50M18 50h16v8H18zM20 42h12v8H20zM38 46h14v12H38zM40 36h10v10H40z"/></svg></div>
    <div class="solution-label" style="left:150px">Investment<br>Management</div>
    <div class="solution-card" style="left:333px"><svg width="64" height="70" viewBox="0 0 64 70" fill="none" stroke="#222" stroke-width="2"><rect x="14" y="8" width="40" height="56" rx="3"/><rect x="26" y="4" width="16" height="8"/><circle cx="18" cy="46" r="10"/><path d="M32 24h16M32 32h16M34 54v-8M40 54v-12M46 54v-6"/></svg></div>
    <div class="solution-label" style="left:333px">Comprehensive<br>Financial Planning</div>
    <div class="solution-card active" style="left:517px"><svg width="64" height="70" viewBox="0 0 64 70" fill="none" stroke="#222" stroke-width="2"><rect x="12" y="6" width="38" height="52"/><path d="M20 16h22M20 24h22M20 32h22"/><rect x="8" y="44" width="30" height="16"/><circle cx="48" cy="52" r="8"/></svg></div>
    <div class="solution-label" style="left:517px">Retirement<br>Income Planning</div>
    <div class="solution-card" style="left:700px"><svg width="64" height="70" viewBox="0 0 64 70" fill="none" stroke="#222" stroke-width="2"><path d="M10 6h30l10 10v44H10z"/><circle cx="24" cy="24" r="8"/><rect x="32" y="38" width="22" height="26"/><path d="M37 46h12M37 52h12M37 58h12M16 54v-8M22 54v-12"/></svg></div>
    <div class="solution-label" style="left:700px">Tax<br>Planning</div>
    <div class="solution-card" style="left:884px"><svg width="64" height="70" viewBox="0 0 64 70" fill="none" stroke="#222" stroke-width="2"><rect x="10" y="10" width="36" height="52"/><rect x="20" y="6" width="16" height="8"/><path d="M18 26h8M30 26h10M18 36h22"/><rect x="34" y="44" width="24" height="18"/><path d="M42 44v-4h8v4"/></svg></div>
    <div class="solution-label" style="left:884px">Estate<br>Planning</div>
  </section>

  <section class="checkup">
    <div class="frame" style="left:700px;top:108px;width:356px;height:309px;border-left:none;border-top:none"></div>
    <div class="photo" role="img" aria-label="Photo of business people silhouetted around a conference table in a bright blue office" style="left:634px;top:78px;width:414px;height:332px;background:linear-gradient(90deg,#7fb2d6 0%,#e6f1f8 35%,#f7d7b3 55%,#c4dcec 75%,#5f93bd 100%)"></div>
  </section>
  <h2 class="checkup-title">The Bulwark $549<br>Retirement Check-Up</h2>
  <div class="divider" style="left:151px;top:2922px"></div>
  <p class="checkup-text" style="top:2936px">We know it's a big decision to hire or switch advisors. That's why<br>we provide an easy way to try us out.&nbsp; At the same time, you can<br>get a valuable second opinion to find out if you're on track to retire.</p>
  <p class="checkup-text" style="top:3020px">There's no pressure &amp; either way, you'll walk away with valuable<br>insights on what you should be doing to secure your future.</p>
  <a class="btn btn-orange" style="left:151px;top:3084px;width:366px;height:44px">Learn more about the $549 Retirement Checkup</a>

  <footer class="site-footer">
    <div class="footer-brand">
      <div class="brand-dot"></div>
      <div><div style="font-size:24px;line-height:24px">BULWARK</div><div style="font-size:12px;padding-left:18px">Asset Advisors</div></div>
    </div>
    <p class="footer-about">With over 55 years of combined experience, Bulwark Asset<br>Advisors helps successful people more effectively prepare<br>for the future.&nbsp; Our unique small team of wealth managers,<br>financial planners &amp; tax professionals bring you the<br>strategies you need to preserve your wealth, minimize your<br>taxes and create a confident retirement. While we're based<br>in Fairmont County, Ohio, we serve clients nationwide.</p>

    <div class="footer-head" style="left:565px">Quick Links</div>
    <ul class="quick-links">
      <li>Home</li><li>Tax Planning</li><li>Our Strategies</li><li>Solutions</li><li>Retirement Check-Up</li><li>Resources</li><li>Contact Us</li>
    </ul>

    <div class="footer-head" style="left:784px">Contact Details</div>
    <div class="contact-row" style="top:97px">
      <div class="contact-icon"><svg width="20" height="22" viewBox="0 0 24 24" fill="none" stroke="#fff" stroke-width="1.6"><path d="M12 22s7-7 7-12a7 7 0 0 0-14 0c0 5 7 12 7 12z"/><circle cx="12" cy="10" r="2.5"/></svg></div>
      <div>123 Lorem Ipsum Dolor Sit<br>Amet, Consectetuer</div>
    </div>
    <div class="contact-row" style="top:179px">
      <div class="contact-icon"><svg width="20" height="20" viewBox="0 0 24 24" fill="none" stroke="#fff" stroke-width="1.6"><path d="M5 3h4l2 5-3 2a12 12 0 0 0 6 6l2-3 5 2v4a2 2 0 0 1-2 2A18 18 0 0 1 3 5a2 2 0 0 1 2-2z"/></svg></div>
      <div>Phone<br>123-456-7890</div>
    </div>
    <div class="contact-row" style="top:251px">
      <div class="contact-icon"><svg width="22" height="18" viewBox="0 0 24 20" fill="none" stroke="#fff" stroke-width="1.6"><rect x="2" y="3" width="20" height="14"/><path d="M2 3l10 8 10-8"/></svg></div>
      <div>Email<br>info@bulwarkassetadvisors.example</div>
    </div>

    <div class="copyright">Copyright © 2021 Bulwark Asset Advisors. All Rights Reserved.</div>
    <div class="badge" role="img" aria-label="Accredited Wealth Steward credential badge"></div>
  </footer>

</div>
</body>
</html>
```